Birchmead Assurance Group Ltd needs a business card and logo

We need a logo for documents, invoices etc and a business card to match. We are a health auditing, training and consulting company based in NZ and working in both Australia and NZ. We ensure health organisations meet all their compliance requirements and develop expertise in the health auditing sector. The design should in some way reflect either symbols for quality management in the health sector.

Target Market(s)

Health providers and those wishing to increase their capability in meeting and understanding compliance requirements

Industry/Entity Type

Business

Contact Information for Business Card

Logo plus contact details

Logo Text

Health auditing, consultancy and training

Requirements
Must have
• Name and contact details director: Clara Hotham, chotham@bag-example.co.nz, PO Box 419, Kowhai Bay, NZ, cell +6427390516

```html
<!DOCTYPE html>
<html lang="en">
<head>
<meta charset="utf-8">
<title>Birchmead Assurance Group Ltd – Business Card</title>
<link href="https://fonts.googleapis.com/css2?family=Open+Sans:wght@400;600;700&display=swap" rel="stylesheet">
<style>
  :root {
    --page-bg: #e9e6e3;
    --card-light: #f1f0ef;
    --green-top: #8fcd3b;
    --green-mid: #4eae28;
    --green-bottom: #168a17;
    --brand-green: #3f9a2a;
    --white: #ffffff;
  }
  * { margin: 0; padding: 0; box-sizing: border-box; }
  html, body {
    width: 1200px;
    height: 900px;
    overflow: hidden;
    background: var(--page-bg);
    font-family: "Open Sans", Arial, sans-serif;
  }
  .business-card {
    position: absolute;
    left: 160px;
    top: 178px;
    width: 880px;
    height: 546px;
    display: flex;
    box-shadow: 0 10px 30px rgba(0,0,0,0.15);
  }
  .brand-side {
    width: 440px;
    height: 100%;
    background: var(--card-light);
    display: flex;
    flex-direction: column;
    align-items: center;
    justify-content: center;
    padding-bottom: 20px;
  }
  .brand-dot {
    width: 72px;
    height: 72px;
    border-radius: 50%;
    background: var(--brand-green);
    margin-bottom: 22px;
  }
  .brand-name {
    color: var(--brand-green);
    font-weight: 600;
    font-size: 30px;
    line-height: 1.2;
    text-align: center;
  }
  .contact-side {
    width: 440px;
    height: 100%;
    background: linear-gradient(180deg, var(--green-top) 0%, var(--green-mid) 55%, var(--green-bottom) 100%);
    color: var(--white);
    padding: 150px 0 0 51px;
  }
  .person-name {
    font-weight: 700;
    font-size: 28px;
    line-height: 1.15;
  }
  .person-role {
    font-size: 21px;
    line-height: 1.3;
  }
  .contact-list {
    list-style: none;
    margin-top: 58px;
  }
  .contact-item {
    display: flex;
    align-items: center;
    font-size: 21px;
    line-height: 32px;
  }
  .contact-icon {
    width: 20px;
    height: 20px;
    margin-right: 12px;
    fill: var(--white);
  }
  .postal-address {
    font-size: 21px;
    margin-top: 34px;
  }
</style>
</head>
<body>
  <main class="business-card">
    <section class="brand-side">
      <div class="brand-dot"></div>
      <p class="brand-name">Birchmead Assurance<br>Group Ltd</p>
    </section>
    <section class="contact-side">
      <p class="person-name">Clara Hotham</p>
      <p class="person-role">Director</p>
      <ul class="contact-list">
        <li class="contact-item">
          <svg class="contact-icon" viewBox="0 0 20 20" aria-hidden="true">
            <path d="M6 1h8a1.5 1.5 0 0 1 1.5 1.5v15A1.5 1.5 0 0 1 14 19H6a1.5 1.5 0 0 1-1.5-1.5v-15A1.5 1.5 0 0 1 6 1zm0.5 2.5v11h7v-11zM10 15.6a1.1 1.1 0 1 0 0 2.2a1.1 1.1 0 0 0 0-2.2z"/>
          </svg>
          +6427390516
        </li>
        <li class="contact-item">
          <svg class="contact-icon" viewBox="0 0 20 20" aria-hidden="true">
            <path d="M4.2 1.5l3 3.3c.4.5.4 1.2 0 1.6L5.8 7.9c1.2 2.6 3.6 5 6.3 6.3l1.5-1.4c.4-.4 1.1-.4 1.6 0l3.3 3c.5.4.5 1.2 0 1.6l-1.6 1.5c-.8.7-2 .9-3 .5C8.5 17.5 2.5 11.5.6 6.1c-.4-1-.2-2.2.5-3l1.5-1.6c.4-.5 1.2-.5 1.6 0z"/>
          </svg>
          chotham@bag-example.co.nz
        </li>
      </ul>
      <p class="postal-address">PO Box 419, Kowhai Bay, NZ</p>
    </section>
  </main>
</body>
</html>
```